Manufacturer of gadgets needs packaging design

We need an outstanding packaging design for our line of cell phone accessories. It needs to be modern, minimalistic design and match our logo

I added a die cut of one of the boxes we are looking to customize with the new design. Winner will have the option to design entire product line

Industry/Entity Type

Cell Phone

Colors
33a6d7
acd036

```html
<!DOCTYPE html>
<html lang="en">
<head>
<meta charset="utf-8">
<title>Mobile Power PB-207 – Box Dieline</title>
<link rel="stylesheet" href="https://fonts.googleapis.com/css2?family=Open+Sans:wght@400;600;700&family=Arimo:wght@400;700&display=swap">
<style>
  :root {
    --paper: #ffffff;
    --board: #6d6e70;
    --fold: #8b8c8e;
    --bar: #a7a9ac;
    --white: #ffffff;
    --ink: #4d4e50;
    --green: #8dc63f;
  }
  html, body { margin: 0; padding: 0; overflow: hidden; background: var(--paper); }
  .canvas {
    position: relative; width: 960px; height: 1200px; overflow: hidden;
    background: var(--paper); font-family: "Open Sans", Arial, sans-serif; color: var(--white);
  }
  .dieline { position: absolute; left: 0; top: 0; }
  .abs { position: absolute; margin: 0; white-space: nowrap; }

  .wordmark { font-weight: 700; letter-spacing: 0.2px; }
  .wordmark .sub { font-weight: 400; border-left: 1px solid currentColor; padding-left: 5px; margin-left: 3px; }

  /* back face */
  .back-title { left: 103px; top: 288px; font-size: 14px; }
  .back-capacity { left: 310px; top: 286px; font-size: 15px; }
  .device-art { position: absolute; left: 100px; top: 320px; width: 128px; height: 170px; background: linear-gradient(135deg, #767779, #7f8082); border-radius: 10px; }
  .model { left: 227px; top: 374px; font-size: 19px; font-weight: 700; }
  .specs { position: absolute; left: 227px; top: 409px; width: 146px; border-collapse: collapse; font-family: "Arimo", Arial, sans-serif; font-size: 8px; color: var(--white); }
  .specs td { padding: 1px 0; border-bottom: 1px solid #9a9b9d; height: 10px; }
  .specs td:first-child { width: 56px; }
  .specs .full td { border-bottom: none; }

  .section-bar { position: absolute; left: 82px; width: 308px; height: 19px; background: var(--bar); font-size: 13px; font-weight: 700; line-height: 19px; text-indent: 9px; }
  .scope-bar { top: 510px; }
  .safety-bar { top: 643px; }

  .scope-icon { position: absolute; top: 550px; border: 1.2px solid var(--white); border-radius: 3px; }
  .scope-caption { position: absolute; top: 604px; margin: 0; width: 60px; font-family: "Arimo", Arial, sans-serif; font-size: 5.5px; line-height: 7px; text-align: center; }

  .safety-list { position: absolute; left: 100px; top: 670px; margin: 0; padding: 0; list-style: none; font-family: "Arimo", Arial, sans-serif; font-size: 7.6px; line-height: 12.4px; }
  .safety-list b { font-weight: 700; }

  .badges { position: absolute; left: 186px; top: 824px; display: flex; gap: 9px; }
  .badge { width: 12px; height: 12px; border-radius: 50%; background: var(--white); }
  .origin { left: 0; width: 472px; top: 845px; text-align: center; font-size: 12.5px; font-weight: 700; }
  .back-footer { left: 103px; top: 904px; font-size: 17px; }
  .back-footer .sub { font-size: 12px; }

  /* side panels */
  .side-mark { font-size: 18px; }
  .side-mark .sub { font-size: 14px; }
  .side-left { left: 448px; top: 615px; transform: translate(-50%, -50%) rotate(90deg); }
  .side-right { left: 873px; top: 615px; transform: translate(-50%, -50%) rotate(-90deg); }

  /* end panels */
  .end-top { left: 560px; top: 214px; font-size: 12px; transform: rotate(180deg); }
  .end-top .sub { font-size: 9px; }
  .end-bottom { left: 560px; top: 1002px; font-size: 12px; }
  .end-bottom .sub { font-size: 9px; }

  /* front face */
  .front-art { position: absolute; left: 497px; top: 268px; width: 326px; height: 694px;
    background: radial-gradient(circle at 62% 88%, #e6ee7a 0%, rgba(230,238,122,0) 35%), linear-gradient(160deg, #cfe03f 0%, #b4d43a 45%, #9bc93c 100%); }
  .front-model { left: 723px; top: 276px; font-size: 14px; }
  .front-band { position: absolute; left: 497px; top: 331px; width: 326px; height: 62px; background: var(--white); text-align: center; color: var(--ink); }
  .front-band .title { display: block; font-size: 26px; font-weight: 700; line-height: 30px; margin-top: 5px; }
  .front-band .subtitle { display: block; font-size: 16px; line-height: 20px; }
  .window { position: absolute; left: 600px; top: 410px; width: 101px; height: 401px; background: var(--white); border: 8px solid var(--green); border-radius: 14px; }
  .brand { left: 497px; width: 326px; top: 878px; text-align: center; font-size: 24px; font-weight: 700; letter-spacing: 1px; color: var(--ink); }
</style>
</head>
<body>
<div class="canvas">

  <svg class="dieline" width="960" height="1200" viewBox="0 0 960 1200" aria-hidden="true">
    <g fill="var(--board)">
      <polygon points="22,300 72,282 72,965 22,948"/>
      <rect x="72" y="75" width="328" height="890"/>
      <path d="M84 75 L90 62 H382 L388 75 Z"/>
      <rect x="400" y="240" width="97" height="725"/>
      <polygon points="400,240 414,198 490,198 497,240"/>
      <polygon points="400,965 414,1008 490,1008 497,965"/>
      <rect x="497" y="170" width="326" height="890"/>
      <path d="M497 170 V145 Q497 115 527 115 H793 Q823 115 823 145 V170 Z"/>
      <path d="M497 1060 V1085 Q497 1115 527 1115 H793 Q823 1115 823 1085 V1060 Z"/>
      <rect x="823" y="240" width="97" height="725"/>
      <polygon points="823,240 830,198 906,198 920,240"/>
      <polygon points="823,965 830,1008 906,1008 920,965"/>
    </g>
    <g fill="var(--paper)">
      <path d="M168 75 H306 Q306 104 270 104 H204 Q168 104 168 75 Z"/>
      <rect x="165" y="192" width="144" height="34" rx="17"/>
    </g>
    <g stroke="var(--fold)" stroke-width="1" fill="none">
      <line x1="72" y1="155" x2="400" y2="155"/>
      <line x1="72" y1="280" x2="400" y2="280"/>
      <line x1="72" y1="282" x2="72" y2="965"/>
      <line x1="400" y1="240" x2="400" y2="965"/>
      <line x1="400" y1="240" x2="497" y2="240"/>
      <line x1="400" y1="965" x2="497" y2="965"/>
      <line x1="497" y1="170" x2="823" y2="170"/>
      <line x1="497" y1="1060" x2="823" y2="1060"/>
      <line x1="823" y1="240" x2="920" y2="240"/>
      <line x1="823" y1="965" x2="920" y2="965"/>
    </g>
  </svg>

  <!-- back face -->
  <p class="abs back-title">MOBILE POWER</p>
  <p class="abs back-capacity">2600mAh</p>
  <div class="device-art" role="img" aria-label="Outline drawing of the power bank stick"></div>
  <p class="abs model">Model: PB-207</p>
  <table class="specs">
    <tr><td>Enter:</td><td>DC 5V-1000mA</td></tr>
    <tr><td>Expert:</td><td>DC5.3V-1000mA(MAX)</td></tr>
    <tr><td>Capacity:</td><td>2600mA</td></tr>
    <tr><td>Volume:</td><td>22*25*100MM</td></tr>
    <tr class="full"><td colspan="2">Executive Standard:&nbsp; GB4706.18-2005</td></tr>
  </table>

  <div class="section-bar scope-bar">Scope</div>
  <div class="scope-icon" style="left:98px;width:32px;height:46px;"></div>
  <div class="scope-icon" style="left:150px;width:36px;height:46px;"></div>
  <div class="scope-icon" style="left:203px;width:36px;height:46px;"></div>
  <div class="scope-icon" style="left:262px;width:126px;height:44px;border-radius:22px;"></div>
  <p class="scope-caption" style="left:84px;">Up to 1.7hrs<br>Extra Run</p>
  <p class="scope-caption" style="left:138px;">Up to 15hrs<br>Extra Talk</p>
  <p class="scope-caption" style="left:191px;">Up to 65hrs<br>Extra Run</p>
  <p class="scope-caption" style="left:295px;">Up to 65hrs<br>Extra Play</p>

  <div class="section-bar safety-bar">Safety Information</div>
  <ul class="safety-list">
    <li>CARGADOR</li>
    <li><b>INCLUYE:</b> Bateria, CableUSB</li>
    <li><b>IMPORTADOR:</b> VOLTA TRADE S.A. de C.V.</li>
    <li><b>RFC</b> VTR080314226</li>
    <li><b>Domicilio Fiscal:</b> Calle Arroyo del Sol, Manzana 27, Lote18-</li>
    <li>Colonia Lomas del Valle- 55090 Estado de Mexico</li>
    <li>Lea el anual antes de usar el equipo</li>
    <li><b>Pais de Origen:</b> China Hecho en China</li>
    <li><b>Tension Nominal de Alta Alimentacion:</b> 100-240 V/AC, 0.15a</li>
    <li><b>Frecuencia nominal de Alimentacion:</b> 56-60 Hz</li>
    <li><b>Tension Potencial Nominal</b> 5.2V/DC 550mA</li>
  </ul>

  <div class="badges">
    <span class="badge"></span><span class="badge"></span><span class="badge"></span><span class="badge"></span><span class="badge"></span>
  </div>
  <p class="abs origin">Designed in Hongkong Made in China</p>
  <p class="abs wordmark back-footer">MOBILE POWER<span class="sub">Mobile power supply</span></p>

  <!-- sides -->
  <p class="abs wordmark side-mark side-left">MOBILE POWER<span class="sub">Mobile power supply</span></p>
  <p class="abs wordmark side-mark side-right">MOBILE POWER<span class="sub">Mobile power supply</span></p>

  <!-- ends -->
  <p class="abs wordmark end-top">MOBILE POWER<span class="sub">Mobile power supply</span></p>
  <p class="abs wordmark end-bottom">MOBILE POWER<span class="sub">Mobile power supply</span></p>

  <!-- front face -->
  <div class="front-art" role="img" aria-label="Green and yellow checkered squares with soft circular light rings"></div>
  <p class="abs front-model">Model: PB-207</p>
  <div class="front-band">
    <span class="title">MOBILE POWER</span>
    <span class="subtitle">Mobile power supply</span>
  </div>
  <div class="window"></div>
  <p class="abs brand">LUMORA</p>

</div>
</body>
</html>
```